Cutting Edge Cloud Hosting Provider needs business card design

We are a new Cloud Hosting Provider called Velkaro Hosting. (Velkaro means cloudy in Spanish.) We provide clients with virtual resources and not virtual machines directly. Our clients purchase the resources that they will use (RAM,CPU, Hard drive space) then use those resources in as many virtual machines as they like.

We are looking for a business card design that is cutting edge and hip.
Updates

The name of the company is "Velkaro Hosting". Please include the "Hosting" part of our name in the design.

Thanks

Target Market(s)

21-35 developers and I.T. Staff

Industry/Entity Type

Business

Requirements
Must have
• Rounded corners, Must Incorporate our logo, individual's name must be prominent

```html
<!DOCTYPE html>
<html lang="en">
<head>
<meta charset="utf-8">
<title>Velkaro Hosting – Business Card</title>
<link rel="stylesheet" href="https://fonts.googleapis.com/css2?family=Roboto+Condensed:wght@400;700&display=swap">
<style>
  :root {
    --page-bg: #e9ecef;
    --card-white: #f7f8fa;
    --blue-light: #5cc0ea;
    --blue-mid: #2f9fd8;
    --blue-deep: #1a78bf;
    --logo-blue: #3f86c4;
    --text-light: #ffffff;
    --divider: rgba(255,255,255,0.55);
  }
  * { margin: 0; padding: 0; box-sizing: border-box; }
  html, body {
    width: 1200px; height: 1023px; overflow: hidden;
    background: var(--page-bg);
    font-family: "Roboto Condensed", Arial, sans-serif;
  }
  .stage {
    width: 1200px; height: 1023px;
    display: flex; align-items: center; justify-content: center;
  }
  .business-card {
    position: relative;
    width: 1050px; height: 600px;
    border-radius: 36px;
    overflow: hidden;
    background: linear-gradient(160deg, var(--blue-light) 0%, var(--blue-mid) 50%, var(--blue-deep) 100%);
    box-shadow: 0 12px 30px rgba(0,0,0,0.18);
  }
  .white-band {
    position: absolute; left: 0; top: 0; width: 100%; height: 100%;
  }
  .arc-texture {
    position: absolute; left: 360px; top: 0; width: 420px; height: 250px;
    background: radial-gradient(ellipse at 60% 0%, rgba(200,210,220,0.35), rgba(247,248,250,0) 70%);
  }
  .brand {
    position: absolute; left: 80px; top: 120px;
    display: flex; align-items: center; gap: 22px;
    color: var(--logo-blue); font-weight: 700;
  }
  .brand-dot {
    width: 34px; height: 34px; border-radius: 50%; background: var(--logo-blue);
  }
  .brand-name { font-size: 92px; line-height: 1; letter-spacing: -1px; }
  .brand-tag { font-size: 22px; letter-spacing: 10px; margin-left: 4px; align-self: flex-end; padding-bottom: 12px; }
  .person {
    position: absolute; left: 80px; bottom: 110px; color: var(--text-light);
  }
  .person-name { font-size: 46px; font-weight: 700; letter-spacing: 1px; text-transform: uppercase; }
  .person-title { font-size: 24px; letter-spacing: 1px; text-transform: uppercase; margin-top: 2px; }
  .website {
    position: absolute; left: 80px; bottom: 62px; color: var(--text-light);
    font-size: 24px; letter-spacing: 1px; text-transform: uppercase;
  }
  .contact {
    position: absolute; right: 70px; bottom: 190px;
    padding-left: 26px; border-left: 2px solid var(--divider);
    color: var(--text-light); font-size: 26px; letter-spacing: 1px;
    text-transform: uppercase; line-height: 1.6;
  }
</style>
</head>
<body>
<main class="stage">
  <section class="business-card">
    <svg class="white-band" viewBox="0 0 1050 600" aria-hidden="true">
      <path d="M0 0 H1050 V150 C820 190 560 300 0 330 Z" fill="var(--card-white)"/>
    </svg>
    <div class="arc-texture" role="img" aria-label="Faint concentric arc texture"></div>
    <div class="brand">
      <span class="brand-dot"></span>
      <span class="brand-name">velkaro</span>
      <span class="brand-tag">HOSTING</span>
    </div>
    <div class="person">
      <div class="person-name">Marco Delgado</div>
      <div class="person-title">Vice-President</div>
    </div>
    <div class="website">W: www.velkaro.com</div>
    <div class="contact">
      <div>P. 210.555.0142</div>
      <div>C. 210.555.0187</div>
      <div>E: marco@velkaro.com</div>
    </div>
  </section>
</main>
</body>
</html>
```